I need a box design created for a DNA Fitness Test

I need a modern and sleek box design for a fitness test. The box needs to have our logo on it and should be clean and modern. The Box is 9 Inches Long 3 and 3/4 inches wide, and 2 inches tall. Company logo attached. The company name is cedar vitality.

Target Market(s)

Fitness

Industry/Entity Type

Fitness

Requirements
Must have
• Our logo

```html
<!DOCTYPE html>
<html lang="en">
<head>
<meta charset="utf-8">
<title>Cedar Vitality – DNA Fitness Test Box</title>
<link href="https://fonts.googleapis.com/css2?family=Montserrat:wght@800&display=swap" rel="stylesheet">
<style>
  :root {
    --backdrop: #e3e6e9;
    --sheet: #ffffff;
    --fold-line: #b9bcbf;
    --ink: #111111;
    --navy: #1c4f86;
    --sky: #4bb8ea;
    --teal: #2aa3a6;
    --lime: #7cc242;
    --mist: #eeeeee;
  }
  * { box-sizing: border-box; margin: 0; padding: 0; }
  html, body {
    width: 1200px; height: 1200px; overflow: hidden;
    background: var(--backdrop);
    font-family: "Montserrat", Arial, sans-serif;
  }
  .dieline {
    position: absolute; left: 100px; top: 172px;
    width: 1000px; height: 856px;
    background: var(--sheet);
    padding: 13px;
    box-shadow: 0 2px 6px rgba(0,0,0,0.08);
  }
  .dieline-frame {
    width: 100%; height: 100%;
    border: 1px solid var(--fold-line);
    display: flex; flex-direction: column;
  }
  .panel { position: relative; overflow: hidden; }
  .panel-top { height: 215px; border-bottom: 1px solid var(--fold-line); }
  .panel-front { height: 402px; border-bottom: 1px solid var(--fold-line); }
  .panel-bottom { flex: 1; }

  .brand {
    position: absolute;
    display: flex; align-items: center; gap: 10px;
    color: var(--ink); font-weight: 800; letter-spacing: 0.5px;
    white-space: nowrap;
  }
  .brand-dot { width: 14px; height: 14px; border-radius: 50%; background: var(--navy); flex: none; }
  .brand-top { left: 50%; top: 50px; font-size: 26px; transform: translateX(-50%) rotate(180deg); }
  .brand-front { left: 42px; top: 140px; font-size: 36px; }
  .brand-bottom { left: 50%; top: 120px; font-size: 26px; transform: translateX(-50%); }

  .dna-art { position: absolute; }
  .dna-top-corner {
    left: 0; top: 0; width: 225px; height: 215px;
    background: linear-gradient(135deg, rgba(124,194,66,0.35), rgba(75,184,234,0.35) 45%, rgba(28,79,134,0.3) 70%, rgba(255,255,255,0) 95%);
  }
  .dna-front-helix {
    left: 0; top: 0; width: 100%; height: 100%;
    background:
      radial-gradient(ellipse at 72% 40%, rgba(124,194,66,0.45), rgba(255,255,255,0) 30%),
      radial-gradient(ellipse at 58% 80%, rgba(28,79,134,0.4), rgba(255,255,255,0) 30%),
      radial-gradient(ellipse at 88% 20%, rgba(42,163,166,0.35), rgba(255,255,255,0) 28%),
      linear-gradient(120deg, rgba(255,255,255,0) 0%, rgba(255,255,255,0) 10%, rgba(238,238,238,0.9) 25%, rgba(75,184,234,0.35) 60%, rgba(238,238,238,0.6) 100%);
  }
  .dna-bottom-corner {
    right: 0; bottom: 0; width: 225px; height: 213px;
    background: linear-gradient(315deg, rgba(124,194,66,0.35), rgba(75,184,234,0.35) 45%, rgba(28,79,134,0.3) 70%, rgba(255,255,255,0) 95%);
  }
</style>
</head>
<body>
  <main class="dieline">
    <div class="dieline-frame">
      <section class="panel panel-top">
        <div class="dna-art dna-top-corner" role="img" aria-label="Diagonal DNA helix of navy, sky blue, teal and green beads in the corner"></div>
        <div class="brand brand-top"><span class="brand-dot"></span>CEDAR VITALITY</div>
      </section>
      <section class="panel panel-front">
        <div class="dna-art dna-front-helix" role="img" aria-label="Large DNA double helix of navy, sky blue, teal and green beads with grey rungs and faint grey bubbles"></div>
        <div class="brand brand-front"><span class="brand-dot"></span>CEDAR VITALITY</div>
      </section>
      <section class="panel panel-bottom">
        <div class="dna-art dna-bottom-corner" role="img" aria-label="Diagonal DNA helix of navy, sky blue, teal and green beads in the corner"></div>
        <div class="brand brand-bottom"><span class="brand-dot"></span>CEDAR VITALITY</div>
      </section>
    </div>
  </main>
</body>
</html>
```